IT Company needs stationary design

Business cards, MS Word, PowerPoint, A4 notepad design base on our company logo. This must be a set of templates in the same style which could be used both for printable documents as well as for documents shared digitally via email, website etc. This should be a modern design which is still professional, so make sure content is well readable both in MS Word and MS PowerPoint templates.

Target Market(s)

SME and Corporate

Industry/Entity Type

It Company

Font styles to use
Sans Serif

Colors
0455a3
0692cd
f37122
ffc214

Requirements
Must have
• 1) Business cards design: modern but still professional
• 2) MS Word: mostly for IT project documents (business analysis, reports, specifications, etc.) must be professional and easy readable.
• 3) MS PowerPoint: first slide, normal slide, last slide.
• 4) A4 notepad: header (must), footer (must), some light design on the background (optionally)
Nice to have
• Business cards design: would be nice to have 2-4 color variations of the same design from one side - cover (for example part of the cards are blue, part of the cards are orange) and other side with contact details is identical.

```html
<!DOCTYPE html>
<html lang="en">
<head>
<meta charset="utf-8">
<title>Nodaris Stationery Set</title>
<link rel="stylesheet" href="https://fonts.googleapis.com/css2?family=Mulish:wght@300;400;600;700&display=swap">
<style>
  :root {
    --backdrop: #e6e6e6;
    --paper: #ffffff;
    --ink: #1c1c1c;
    --card-dark: #0a0b0d;
    --brand-blue: #00a1e0;
    --sky: #7fcde6;
    --orange: #f37122;
    --yellow: #f5b800;
    --rule: #cfcfcf;
    --watermark: #f0f0f0;
    --muted: #555;
  }
  * { box-sizing: border-box; margin: 0; padding: 0; }
  html, body { width: 1200px; height: 938px; overflow: hidden; }
  body {
    background: var(--backdrop);
    font-family: "Mulish", sans-serif;
    color: var(--ink);
    position: relative;
  }

  /* Brand lockup: plain circle + wordmark */
  .brand { display: flex; align-items: center; gap: 8px; font-weight: 300; letter-spacing: 0.5px; }
  .brand-dot { border-radius: 50%; border: 2px solid currentColor; flex: none; }

  /* Business card front */
  .card-front {
    position: absolute; left: 182px; top: 308px; width: 235px; height: 142px;
    background: var(--card-dark); color: #fff;
  }
  .card-front .brand { position: absolute; left: 40px; top: 50px; font-size: 21px; color: #fff; }
  .card-front .brand-dot { width: 36px; height: 36px; }
  .card-front .site {
    position: absolute; left: 0; right: 0; top: 128px;
    display: flex; justify-content: center; align-items: center; gap: 6px;
    font-size: 6px; letter-spacing: 1px; color: #fff;
  }
  .card-front .site .line { width: 18px; height: 1px; background: var(--brand-blue); }
  .card-front .site em { font-style: normal; color: var(--brand-blue); }

  /* Business card back */
  .card-back {
    position: absolute; left: 182px; top: 487px; width: 235px; height: 141px;
    background: var(--paper);
  }
  .card-back .brand-stack {
    position: absolute; left: 20px; top: 40px; width: 95px;
    display: flex; flex-direction: column; align-items: center; gap: 7px;
    font-weight: 300; font-size: 17px; letter-spacing: 0.5px; color: var(--ink);
  }
  .card-back .brand-dot { width: 36px; height: 36px; }
  .contact { position: absolute; left: 134px; top: 33px; }
  .contact .name { font-size: 10px; font-weight: 700; color: var(--brand-blue); }
  .contact .role { font-size: 5.5px; margin-top: 2px; color: var(--ink); }
  .contact ul { list-style: none; margin-top: 9px; font-size: 5.5px; line-height: 8.5px; }
  .contact li { display: flex; align-items: center; gap: 5px; }
  .contact li svg { width: 5px; height: 5px; fill: var(--orange); flex: none; }
  .contact li em { font-style: normal; color: var(--brand-blue); }
  .contact .address { margin-top: 1px; font-size: 5.5px; line-height: 7.5px; }
  .color-bar { position: absolute; left: 0; bottom: 0; width: 100%; height: 3px; display: flex; }
  .color-bar span { flex: 1; }

  /* Letterhead */
  .letterhead {
    position: absolute; left: 474px; top: 85px; width: 543px; height: 768px;
    background: #fafafa; overflow: hidden;
  }
  .letterhead .watermark {
    position: absolute; left: 76px; top: 110px; width: 520px; height: 520px;
    border: 26px solid var(--watermark); border-radius: 50%;
  }
  .letterhead .brand {
    position: absolute; left: 0; right: 0; top: 24px; justify-content: center;
    font-size: 28px; color: var(--ink); gap: 12px;
  }
  .letterhead .brand-dot { width: 52px; height: 52px; border-width: 3px; }
  .ruled {
    position: absolute; left: 38px; top: 104px; width: 468px; height: 600px;
    background: repeating-linear-gradient(to bottom, var(--rule) 0 1px, transparent 1px 19.3px);
  }
  .letter-footer {
    position: absolute; left: 0; bottom: 0; width: 100%; height: 39px;
    background: var(--brand-blue); color: #fff;
    display: flex; flex-direction: column; align-items: center; justify-content: center;
    font-size: 8px; line-height: 11px;
  }
  .letter-footer .row { display: flex; align-items: center; gap: 4px; }
  .letter-footer svg { width: 7px; height: 7px; fill: #fff; }
</style>
</head>
<body>

  <section class="card-front" aria-label="Business card front">
    <div class="brand"><span class="brand-dot"></span>nodaris</div>
    <div class="site"><span class="line"></span>www.<em>nodaris</em>.com<span class="line"></span></div>
  </section>

  <section class="card-back" aria-label="Business card back">
    <div class="brand-stack"><span class="brand-dot"></span>nodaris</div>
    <div class="contact">
      <p class="name">Mara Lindqvist</p>
      <p class="role">Managing Director</p>
      <ul>
        <li><svg viewBox="0 0 10 10"><path d="M2 1h2l1 2.5-1.3 1a6 6 0 0 0 2.8 2.8l1-1.3L10 7v2c0 .6-.4 1-1 1A9 9 0 0 1 0 1c0-.6.4-1 1-1z"/></svg>555.204.7781</li>
        <li><svg viewBox="0 0 10 10"><path d="M0 2h10v6H0zM1 3l4 3 4-3"/></svg>mara@nodaris.com</li>
        <li><svg viewBox="0 0 10 10"><circle cx="5" cy="5" r="5"/></svg>www.<em>nodaris</em>.com</li>
      </ul>
      <p class="address">18 Harbor Lane,<br>Eastfield, US 40212</p>
    </div>
    <div class="color-bar">
      <span style="background:var(--brand-blue)"></span>
      <span style="background:var(--sky)"></span>
      <span style="background:var(--orange)"></span>
      <span style="background:var(--yellow)"></span>
    </div>
  </section>

  <section class="letterhead" aria-label="A4 notepad">
    <div class="watermark"></div>
    <div class="brand"><span class="brand-dot"></span>nodaris</div>
    <div class="ruled"></div>
    <footer class="letter-footer">
      <div class="row">
        <svg viewBox="0 0 10 10"><path d="M2 1h2l1 2.5-1.3 1a6 6 0 0 0 2.8 2.8l1-1.3L10 7v2c0 .6-.4 1-1 1A9 9 0 0 1 0 1c0-.6.4-1 1-1z"/></svg>555.204.7781
        &nbsp;<svg viewBox="0 0 10 10"><path d="M0 2h10v6H0z"/></svg>mara@nodaris.com
        &nbsp;<svg viewBox="0 0 10 10"><circle cx="5" cy="5" r="5"/></svg>www.nodaris.com
      </div>
      <div>18 Harbor Lane, Eastfield, US 40212</div>
    </footer>
  </section>

</body>
</html>
```